Patient information leaflets

Hi - We need a template design for pathology specific patient information leaflets to be printed as necessary in clinic on a desktop printer. Text and pictures to be pasted/updated by the treating clinician. Format either A4 landscape with 2 A5 pages per sheet or straight forward A4, to be folded and presented in our previously designed A5 folder. Branded as per the folder. Title Page and follow on pages. E.g. title 'Back Pain'.

Essentials:
Web address
enquiries@carewell-example.org.uk
Mendora Logo
'Working in Partnership with the PCB'
'Copyright Mendora Ltd 2014'.

```html
<!DOCTYPE html>
<html lang="en">
<head>
<meta charset="utf-8">
<title>Managing Knee Pain – Mendora Patient Leaflet</title>
<link rel="stylesheet" href="https://fonts.googleapis.com/css2?family=Arimo:wght@400;500;600&display=swap">
<style>
  :root {
    --canvas: #ececec;
    --paper: #ffffff;
    --brand-orange: #f15a22;
    --ink: #111111;
    --navy: #1c2340;
    --muted: #555555;
    --band-light: #fbfbfb;
    --band-mid: #efefef;
    --band-edge: #e2e2e2;
    --badge-grey: #c9c9c9;
  }
  * { margin: 0; padding: 0; box-sizing: border-box; }
  html, body {
    width: 1200px;
    height: 806px;
    overflow: hidden;
    background: var(--canvas);
    font-family: "Arimo", Arial, sans-serif;
  }
  .leaflet {
    position: absolute;
    left: 60px;
    top: 22px;
    width: 1080px;
    height: 762px;
    background: var(--paper);
    overflow: hidden;
  }
  .brand-name {
    position: absolute;
    right: 34px;
    top: 60px;
    font-size: 30px;
    font-weight: 400;
    line-height: 34px;
    color: var(--navy);
    letter-spacing: -0.3px;
  }
  .feature-band {
    position: absolute;
    left: 0;
    top: 142px;
    width: 100%;
    height: 463px;
  }
  .back-panel {
    position: absolute;
    left: 0;
    top: 0;
    width: 538px;
    height: 100%;
    background: linear-gradient(90deg, var(--band-edge) 0%, var(--band-mid) 30%, var(--band-light) 100%);
  }
  .spine {
    position: absolute;
    left: 538px;
    top: 0;
    width: 37px;
    height: 100%;
    background: var(--brand-orange);
  }
  .cover-panel {
    position: absolute;
    left: 575px;
    top: 0;
    right: 0;
    height: 100%;
    background: linear-gradient(90deg, var(--paper) 0%, var(--band-light) 40%, var(--band-edge) 100%);
  }
  .clinic-details {
    position: absolute;
    left: 0;
    width: 538px;
    top: 212px;
    text-align: center;
    color: var(--navy);
  }
  .clinic-name {
    font-size: 19px;
    line-height: 22px;
  }
  .clinic-contact {
    font-size: 11.5px;
    line-height: 14px;
  }
  .leaflet-title {
    position: absolute;
    left: 575px;
    right: 0;
    top: 210px;
    text-align: center;
    font-size: 36px;
    font-weight: 600;
    color: var(--ink);
    letter-spacing: -0.4px;
  }
  .leaflet-title .topic { color: var(--brand-orange); }
  .partner {
    position: absolute;
    left: 0;
    width: 544px;
    top: 656px;
    text-align: center;
  }
  .partner-badge {
    display: block;
    width: 42px;
    height: 42px;
    margin: 0 auto;
    border-radius: 50%;
    background: var(--badge-grey);
  }
  .partner-text {
    margin-top: 12px;
    font-size: 12px;
    color: var(--muted);
  }
  .tagline {
    position: absolute;
    right: 32px;
    top: 700px;
    font-size: 21px;
    color: var(--brand-orange);
  }
  .footer-bar {
    position: absolute;
    left: 0;
    bottom: 0;
    width: 100%;
    height: 11px;
    background: var(--brand-orange);
  }
</style>
</head>
<body>
  <main class="leaflet">
    <p class="brand-name">Mendora</p>

    <section class="feature-band">
      <div class="back-panel"></div>
      <div class="spine"></div>
      <div class="cover-panel"></div>
      <div class="clinic-details">
        <p class="clinic-name">Mendora Community Clinics</p>
        <p class="clinic-contact">www.carewell-example.org.uk | enquiries@carewell-example.org.uk</p>
      </div>
      <h1 class="leaflet-title">Managing <span class="topic">Knee Pain</span></h1>
    </section>

    <div class="partner">
      <span class="partner-badge" role="img" aria-label="Partner badge"></span>
      <p class="partner-text">Working in partnership with the PCB</p>
    </div>

    <p class="tagline">Your health. Your care.</p>
    <div class="footer-bar"></div>
  </main>
</body>
</html>
```